Sales folder

We desire a folder in which to insert documents and sales flyers into. The picture attached is the cover of our current sales folder, while we like it, it is out dated. We would like to keep close to what we have but with newer information on the inside. The pockets on the inside are vertical pockets and there is a business card holder on the right side. The back is all black with our contact information on the bottom.

Target Market(s)

Information technology

Industry/Entity Type

Information Technology

Font styles to use
Sans Serif

Colors
acd037

Requirements
Must have
• similar look and feel

```html
<!DOCTYPE html>
<html lang="en">
<head>
<meta charset="utf-8">
<title>Brightlane Sales Folder</title>
<link href="https://fonts.googleapis.com/css2?family=Montserrat:wght@400;600;700&display=swap" rel="stylesheet">
<style>
  :root{
    --lime:#acd037;
    --green:#95b84b;
    --green-deep:#7f9e2c;
    --tint:#eef5dc;
    --ink:#1e1d1e;
    --grey:#555;
    --paper:#ffffff;
    --stage:#8c8c8c;
  }
  *{margin:0;padding:0;box-sizing:border-box}
  html,body{width:1200px;height:1200px;overflow:hidden}
  body{background:var(--stage);font-family:'Montserrat',sans-serif;position:relative}
  .spread{position:absolute;left:210px;display:flex;box-shadow:0 10px 30px rgba(0,0,0,.25)}
  .spread--outside{top:40px}
  .spread--inside{top:630px;left:225px}
  .panel{width:375px;height:520px;background:var(--paper);position:relative;overflow:hidden}
  .spine{width:30px;height:520px;background:var(--ink)}
  .brand{display:flex;align-items:center;gap:8px;font-weight:700;letter-spacing:.08em;text-transform:lowercase}
  .brand__square{width:16px;height:16px;background:var(--lime)}
  .brand__name{color:var(--ink)}
  .brand--light .brand__name{color:#fff}
  .brand--light .brand__square{background:#fff}

  /* back cover */
  .back__pattern{position:absolute;inset:0;background:linear-gradient(180deg,var(--tint) 0%,#fbfdf5 55%,var(--tint) 100%)}
  .back__contact{position:absolute;left:0;right:0;bottom:40px;display:flex;flex-direction:column;align-items:center;gap:6px;font-size:11px;color:var(--grey);text-align:center}
  .back__contact .brand{font-size:22px;margin-bottom:10px}
  .contact__company{color:var(--green-deep);font-weight:600}
  .contact__icon{width:12px;height:12px;margin-top:4px}

  /* front cover */
  .front .brand{position:absolute;top:36px;left:50%;transform:translateX(-50%);font-size:18px}
  .front__art{position:absolute;left:40px;right:0;top:90px;height:330px;background:radial-gradient(circle at 65% 45%,var(--green-deep) 0%,var(--lime) 30%,var(--tint) 65%,#fff 100%)}
  .front__url{position:absolute;right:0;bottom:28px;width:180px;height:30px;background:var(--ink);color:#ddd;font-size:10px;letter-spacing:.08em;display:flex;align-items:center;justify-content:center;border-top-left-radius:16px}

  /* inside */
  .inside-left{background:linear-gradient(90deg,#fff 55%,#e4e4e4 100%)}
  .pocket-left{position:absolute;left:0;bottom:0;width:375px;height:220px}
  .pocket-left .brand{position:absolute;left:80px;bottom:70px;font-size:20px}
  .inside-right .brand{position:absolute;top:180px;left:50%;transform:translateX(-50%);font-size:26px}
  .pocket-right{position:absolute;left:0;bottom:0;width:375px;height:250px}
  .card-slot{position:absolute;left:150px;bottom:110px;width:190px;height:100px;background:var(--ink)}
  .card{position:absolute;left:160px;bottom:85px;width:170px;height:95px;background:#fff;border-bottom:14px solid var(--lime);display:flex;flex-direction:column;align-items:center;justify-content:center;gap:8px}
  .card .brand{position:static;transform:none;font-size:12px}
  .card__url{font-size:8px;letter-spacing:.15em;color:var(--ink)}
</style>
</head>
<body>

<section class="spread spread--outside">
  <div class="panel back">
    <div class="back__pattern" role="img" aria-label="Faint light-green circuit-line pattern"></div>
    <div class="back__contact">
      <div class="brand"><span class="brand__square"></span><span class="brand__name">Brightlane</span></div>
      <svg class="contact__icon" viewBox="0 0 12 12"><circle cx="6" cy="6" r="6" fill="#acd037"/><path d="M6 2.5a2.3 2.3 0 0 0-2.3 2.3C3.7 6.6 6 9.5 6 9.5s2.3-2.9 2.3-4.7A2.3 2.3 0 0 0 6 2.5z" fill="#fff"/></svg>
      <span class="contact__company">Brightlane</span>
      <span>214 Harbor Lane<br>Millbrook, MI 48000</span>
      <svg class="contact__icon" viewBox="0 0 12 12"><circle cx="6" cy="6" r="6" fill="#acd037"/><rect x="4" y="3" width="4" height="6" rx="1" fill="#fff"/></svg>
      <span>(800) 555-0142</span>
      <svg class="contact__icon" viewBox="0 0 12 12"><circle cx="6" cy="6" r="6" fill="#acd037"/><rect x="4" y="3" width="4" height="6" rx="1" fill="#fff"/></svg>
      <span>(555) 310-2277</span>
      <svg class="contact__icon" viewBox="0 0 12 12"><circle cx="6" cy="6" r="6" fill="#acd037"/><circle cx="6" cy="6" r="3" fill="none" stroke="#fff" stroke-width="1"/></svg>
      <span>www.gobrightlane.com</span>
    </div>
  </div>
  <div class="spine"></div>
  <div class="panel front">
    <div class="brand"><span class="brand__square"></span><span class="brand__name">Brightlane</span></div>
    <div class="front__art" role="img" aria-label="Green technical illustration of interlocking gears with circuit lines and arrows"></div>
    <div class="front__url">www.gobrightlane.com</div>
  </div>
</section>

<section class="spread spread--inside">
  <div class="panel inside-left">
    <div class="pocket-left">
      <svg width="375" height="220" viewBox="0 0 375 220"><path d="M0 220 V140 C60 50 180 20 300 50 C340 60 360 80 375 110 V220 Z" fill="#95b84b"/></svg>
      <div class="brand brand--light"><span class="brand__square"></span><span class="brand__name">Brightlane</span></div>
    </div>
  </div>
  <div class="panel inside-right">
    <div class="brand"><span class="brand__square"></span><span class="brand__name">Brightlane</span></div>
    <div class="pocket-right">
      <svg width="375" height="250" viewBox="0 0 375 250"><path d="M40 250 V110 C40 70 65 50 105 50 L375 0 V250 Z" fill="#95b84b"/></svg>
      <div class="card-slot"></div>
      <div class="card">
        <div class="brand"><span class="brand__square"></span><span class="brand__name">Brightlane</span></div>
        <span class="card__url">www.gobrightlane.com</span>
      </div>
    </div>
  </div>
</section>

</body>
</html>
```